Mobile Home Page Design for “Zarvo for Plumbers” – in Figma

PipeDashly: Fast, Reliable Emergency Plumbing at Your Fingertips

PipeDashly is a streamlined platform connecting homeowners with trusted, local plumbers for urgent repairs—whether it’s a burst pipe, leak, or blocked toilet. Designed for speed and peace of mind, our homepage will be clean, modern, and mobile-optimized to guide users from problem to solution in minutes.

Our primary users are homeowners in stressful situations who care most about price transparency and how fast help can arrive. Bookings are made exclusively online, so the user experience must instill confidence and eliminate hesitation.

The call-to-action should be immediate and persuasive—"See Prices & Book" will be prominently featured as the main CTA. Additional trust-builders could include:

A simple 3-step booking illustration (Tell us what’s wrong → See prices → Get a plumber)
Customer reviews or “Trusted by 10,000+ homeowners” badges

Display real-time availability ("Next plumber available in 40 minutes")
Price estimates upfront—with clear service types

Target Market(s)

Home Owners: 35-65 Years old.

Industry/Entity Type

Home Services.

Number of Pages Required

1 page

Font styles to use
Sans Serif

Colors
0054AA
0677BA
7BADD7
CADEEF
E8F1F8
FFF300
FFF600
FEFA6F
FFFEC7
FFFEE8

Requirements
Nice to have
• Map showing that plumbers are nearby. Trustworthy look and feel. Blue/Red or Blue/Yellow.

```html
<!DOCTYPE html>
<html lang="en">
<head>
<meta charset="utf-8">
<title>PipeDashly – Mobile Home Page</title>
<link href="https://fonts.googleapis.com/css2?family=Poppins:wght@400;500;600;700&display=swap" rel="stylesheet">
<style>
:root{
  --stage:#8f8f8f;
  --blue:#2561a3;
  --blue-dark:#1d4f8a;
  --blue-light:#7badd7;
  --blue-pale:#e8f1f8;
  --badge:#cadeef;
  --grey-band:#efeff0;
  --text:#1b1b1b;
  --white:#fff;
  --star:#f5c400;
}
*{box-sizing:border-box;margin:0;padding:0}
html,body{width:1200px;height:3812px;overflow:hidden}
body{background:var(--stage);font-family:'Poppins',sans-serif;color:var(--text);position:relative}
.screen{position:absolute;top:115px;width:375px;background:var(--white);overflow:hidden}
.screen--home{left:198px;height:3581px}
.screen--more{left:627px;height:2611px}
.section{position:relative;display:flex;flex-direction:column;align-items:center}
.heading{font-weight:600;font-size:16px;text-align:center;line-height:1.35;letter-spacing:.2px}
.heading::after{content:"";display:block;width:48px;height:2px;margin:8px auto 0;background:
  radial-gradient(circle,var(--blue) 3px,transparent 3.5px) center/8px 8px no-repeat,var(--blue-light)}
.btn{display:inline-flex;align-items:center;justify-content:center;background:var(--blue);color:var(--white);font-weight:600;border-radius:4px;text-transform:uppercase}
.btn--sm{font-size:6.5px;height:22px;padding:0 16px}
.photo{border-radius:12px}

/* header + hero */
.topbar{height:70px;background:var(--blue);display:flex;align-items:center;justify-content:space-between;padding:0 22px}
.brand{color:var(--white);font-weight:600;font-size:22px}
.burger{width:56px;height:28px;display:flex;flex-direction:column;justify-content:space-between}
.burger span{height:2px;background:var(--white)}
.hero{height:311px;background:linear-gradient(135deg,#4a5766,#27313d 55%,#1a2129)}
.hero-panel{position:absolute;left:21px;right:21px;top:52px;height:207px;background:rgba(37,97,163,.85);border-radius:6px;display:flex;flex-direction:column;align-items:center;padding-top:22px;color:var(--white)}
.hero-panel h1{font-size:21px;font-weight:600;text-align:center;line-height:1.3}
.hero-panel .btn{margin:14px 0 18px;background:#3b7ccc;font-size:12px;height:30px;width:162px;border-radius:3px}
.hero-panel p{font-size:11px;text-align:center;line-height:1.75}

/* trust */
.trust{height:200px;padding-top:38px}
.trust-row{display:flex;gap:14px;margin-top:22px}
.trust-card{width:96px;height:90px;background:var(--white);box-shadow:0 1px 5px rgba(0,0,0,.18);border-radius:3px;display:flex;flex-direction:column;align-items:center;padding-top:10px}
.trust-card .ico{width:40px;height:40px;border-radius:50%;background:var(--blue);border:3px solid var(--blue-pale);outline:1px solid var(--blue)}
.trust-card span{font-size:8.5px;text-align:center;line-height:1.25;margin-top:7px}

/* services */
.services{height:1040px;padding-top:14px}
.service{display:flex;flex-direction:column;align-items:center;margin-top:40px}
.service + .service{margin-top:30px}
.service .photo{width:242px;height:178px}
.service h3{color:var(--blue);font-size:16px;font-weight:500;margin-top:18px}
.service p{font-size:8.5px;text-align:center;line-height:1.9;margin:6px 0 10px}
.ph-plumbing{background:linear-gradient(135deg,#4d6a7e,#a9b4b6 55%,#6e5448)}
.ph-heating{background:linear-gradient(135deg,#c9cfd3,#ececec 50%,#9da4ab)}
.ph-drain{background:linear-gradient(135deg,#6e6a63,#d4d0c8 45%,#26509a)}

/* zarvo band */
.zarvo{height:438px;background:var(--blue);color:var(--white);padding-top:42px}
.zarvo .heading{color:var(--white)}
.zarvo .heading::after{display:none}
.checks{list-style:none;margin-top:18px}
.checks li{font-size:9.5px;display:flex;align-items:center;gap:8px;margin-bottom:8px}
.checks svg{flex:none}
.zarvo .photo{width:268px;height:175px;border-radius:4px;margin-top:8px;background:linear-gradient(135deg,#3d4652,#8f3a22 45%,#2f6bb8)}
.zarvo .track{margin-top:20px;width:264px;height:28px;background:var(--white);color:var(--blue);font-size:10px;font-weight:600;display:flex;align-items:center;justify-content:center;border-radius:2px}

/* call */
.call{height:364px;padding-top:42px}
.call .heading::after{display:none}
.call .sub{font-size:8.5px;margin-top:14px}
.map{width:333px;height:178px;margin-top:12px;border-radius:8px;background:linear-gradient(160deg,#d9dde0,#c3c8cc 50%,#e3e5e7)}
.call .btn{margin-top:16px;width:112px}

/* why */
.why{height:1157px;background:var(--grey-band);padding-top:40px}
.why .photo{width:268px;height:175px;border-radius:4px;margin-top:14px;background:linear-gradient(135deg,#c9ced3,#3e6bb0 50%,#e9e9e9)}
.perk{display:flex;flex-direction:column;align-items:center;margin-top:44px}
.perk--first{margin-top:28px}
.ring{width:190px;height:190px;border-radius:50%;border:2px dotted var(--blue);display:flex;align-items:center;justify-content:center}
.ring .core{width:163px;height:163px;border-radius:50%;background:var(--blue);display:flex;align-items:center;justify-content:center}
.perk h4{font-weight:400;font-size:28px;margin-top:10px;letter-spacing:.3px}

/* right screen */
.accreds{height:721px;padding-top:45px}
.badges{display:grid;grid-template-columns:162px 162px;gap:14px 10px}
.badge{height:88px;background:var(--white);box-shadow:0 1px 5px rgba(0,0,0,.18);border-radius:3px;display:flex;align-items:center;justify-content:center}
.badge i{display:block;width:110px;height:44px;border-radius:6px;background:var(--badge)}
.accreds .heading{margin-top:52px}
.boroughs{margin-top:22px;width:333px;height:287px;background:var(--blue);border-radius:12px;display:grid;grid-template-columns:1fr 1fr;padding:22px 20px 0 30px}
.boroughs ul{list-style:none}
.boroughs li{color:var(--white);font-size:8px;line-height:15px;position:relative;padding-left:14px}
.boroughs li::before{content:"";position:absolute;left:0;top:6px;width:4px;height:4px;border-radius:50%;background:var(--white)}

.feedback{height:404px;background:var(--grey-band);padding-top:36px}
.feedback .heading::after{display:none}
.feedback .sub{font-size:8.5px;text-align:center;line-height:1.8;margin-top:12px}
.review{width:315px;height:200px;background:var(--white);box-shadow:0 1px 4px rgba(0,0,0,.1);margin-top:12px;display:flex;flex-direction:column;align-items:center;padding-top:14px}
.review .quote{color:var(--blue);font-size:80px;font-weight:700;line-height:.8;height:44px;font-family:Georgia,serif}
.review p{font-size:8.5px;text-align:center;line-height:1.95;padding:0 22px;margin-top:10px}
.review .name{color:var(--blue);font-weight:500;font-size:11px;margin-top:8px}
.review .stars{color:var(--star);font-size:11px;letter-spacing:3px}
.dots{display:flex;gap:4px;margin-top:24px}
.dots span{width:9px;height:9px;border-radius:50%;border:1.5px solid var(--blue)}
.dots span:first-child{background:var(--blue)}

.faq{height:540px;padding-top:38px}
.faq-list{list-style:none;margin-top:18px;width:318px}
.faq-list li{height:32px;margin-bottom:9px;box-shadow:0 1px 4px rgba(0,0,0,.15);display:flex;align-items:center;justify-content:space-between;padding:0 10px 0 16px;font-size:8px;font-weight:500}
.faq-list li.open{background:var(--blue);color:var(--white)}
.faq-list .pm{width:10px;height:10px;border-radius:50%;border:1.5px solid var(--blue);position:relative;flex:none}
.faq-list .pm::before,.faq-list .pm::after{content:"";position:absolute;background:var(--blue);left:2px;right:2px;top:3.5px;height:1.5px}
.faq-list .pm::after{left:3.5px;right:auto;width:1.5px;top:2px;height:5px}
.faq-list li.open .pm{background:var(--white);border-color:var(--white)}
.faq-list li.open .pm::after{display:none}
.faq .btn{margin-top:18px;width:78px}

.footer{height:946px;background:var(--blue);color:var(--white);align-items:flex-start;padding:38px 20px 0}
.footer .brand{font-size:22px}
.f-lines{font-size:9px;line-height:22px;margin-top:12px}
.heart{display:inline-block;width:7px;height:7px;border-radius:50%;background:#e2242b}
.iso{display:flex;align-items:center;gap:26px;margin-top:24px}
.iso i{display:block;width:94px;height:94px;border-radius:50%;border:2px solid var(--white)}
.iso span{font-size:16px;font-weight:500}
.f-head{font-size:16px;font-weight:600;margin-top:36px;border-bottom:1.5px solid var(--white);padding-bottom:2px}
.addr{display:flex;gap:12px;align-items:center;margin-top:20px;font-size:7.5px;line-height:1.6}
.addr b{width:20px;height:20px;border:1.5px solid var(--white);border-radius:3px;display:flex;align-items:center;justify-content:center}
.f-cols{display:flex;gap:40px}
.f-cols ul{list-style:none;margin-top:18px}
.dotlist li{font-size:9px;line-height:22px;padding-left:14px;position:relative}
.dotlist li::before{content:"";position:absolute;left:0;top:9px;width:4px;height:4px;border-radius:50%;background:var(--white)}
.social li{font-size:8px;line-height:30px;display:flex;align-items:center;gap:8px}
.social i{width:16px;height:16px;background:#3b7ccc;border-radius:3px}
.apps{display:flex;gap:10px;margin-top:26px;background:#1a3f6e;padding:6px 8px}
.apps span{width:78px;height:24px;background:#000;border:1px solid #999;border-radius:3px;font-size:8px;display:flex;align-items:center;justify-content:center}
.legal{font-size:8px;font-weight:500;line-height:15px;margin-top:20px;width:200px}
.policies{list-style:none;margin-top:14px}
.policies li{line-height:22px}
.copybar{position:absolute;left:0;right:0;bottom:0;height:35px;background:var(--blue-dark);font-size:8px;display:flex;align-items:center;padding-left:20px}
</style>
</head>
<body>

<main class="screen screen--home">
  <header class="topbar">
    <span class="brand">PipeDashly</span>
    <div class="burger"><span></span><span></span><span></span></div>
  </header>

  <section class="section hero" role="img" aria-label="Photo of a plumber working under a sink">
    <div class="hero-panel">
      <h1>BOOK A PLUMBER NEAR<br>YOU - FAST</h1>
      <span class="btn">BOOK NOW</span>
      <p>Get an instant response from<br>a trusted plumber 24/7</p>
    </div>
  </section>

  <section class="section trust">
    <h2 class="heading">ALL OUR PLUMBERS ARE</h2>
    <div class="trust-row">
      <div class="trust-card"><div class="ico"><svg viewBox="0 0 40 40" width="34" height="34"><circle cx="20" cy="16" r="4" fill="#fff"/><circle cx="12" cy="18" r="3" fill="#fff"/><circle cx="28" cy="18" r="3" fill="#fff"/><path d="M13 28a7 7 0 0 1 14 0z M6 28a6 6 0 0 1 10-4 M34 28a6 6 0 0 0-10-4" fill="#fff"/></svg></div><span>Experienced<br>Plumbers</span></div>
      <div class="trust-card"><div class="ico"><svg viewBox="0 0 40 40" width="34" height="34"><circle cx="20" cy="20" r="9" fill="none" stroke="#fff" stroke-width="3" stroke-dasharray="4 2"/><path d="M16 20l3 3 5-6" fill="none" stroke="#fff" stroke-width="2"/></svg></div><span>Verified<br>Credentials</span></div>
      <div class="trust-card"><div class="ico"><svg viewBox="0 0 40 40" width="34" height="34"><path d="M20 9l9 3v7c0 6-4 10-9 12-5-2-9-6-9-12v-7z" fill="#fff"/><path d="M16 20l3 3 5-6" fill="none" stroke="#2561a3" stroke-width="2"/></svg></div><span>Fully Insured<br>Plumbers</span></div>
    </div>
  </section>

  <section class="section services">
    <h2 class="heading">FEATURED SERVICES</h2>
    <article class="service">
      <div class="photo ph-plumbing" role="img" aria-label="Photo of a plumber fixing a kitchen tap"></div>
      <h3>PLUMBING</h3>
      <p>We offer all solutions to all your plumbing<br>problems from leaks to blocked toilets</p>
      <span class="btn btn--sm">READ MORE</span>
    </article>
    <article class="service">
      <div class="photo ph-heating" role="img" aria-label="Photo of an engineer servicing a wall boiler"></div>
      <h3>HEATING</h3>
      <p>We offer all solutions to all your plumbing<br>problems from leaks to blocked toilets</p>
      <span class="btn btn--sm">READ MORE</span>
    </article>
    <article class="service">
      <div class="photo ph-drain" role="img" aria-label="Photo of a plumber clearing a drain under a sink"></div>
      <h3>DRAINAGE</h3>
      <p>We offer all solutions to all your plumbing<br>problems from leaks to blocked toilets</p>
      <span class="btn btn--sm">READ MORE</span>
    </article>
  </section>

  <section class="section zarvo">
    <h2 class="heading">WE’RE LIKE ZARVO – FOR PLUMBERS</h2>
    <ul class="checks">
      <li><svg width="12" height="12" viewBox="0 0 12 12"><circle cx="6" cy="6" r="5.2" fill="none" stroke="#fff"/><path d="M3.5 6l2 2 3-3.5" fill="none" stroke="#fff"/></svg>Select your issue</li>
      <li><svg width="12" height="12" viewBox="0 0 12 12"><circle cx="6" cy="6" r="5.2" fill="none" stroke="#fff"/><path d="M3.5 6l2 2 3-3.5" fill="none" stroke="#fff"/></svg>View our pricing</li>
      <li><svg width="12" height="12" viewBox="0 0 12 12"><circle cx="6" cy="6" r="5.2" fill="none" stroke="#fff"/><path d="M3.5 6l2 2 3-3.5" fill="none" stroke="#fff"/></svg>Get an instant response &amp; Book</li>
    </ul>
    <div class="photo" role="img" aria-label="Photo of a plumber in a hard hat working on a boiler system"></div>
    <span class="track">TRACK YOUR PLUMBER EN ROUTE TO YOU</span>
  </section>

  <section class="section call">
    <h2 class="heading">CALL AN PIPEDASHLY PLUMBER NOW</h2>
    <p class="sub">We have plumbers near you ready to assist 24/7.</p>
    <div class="map" role="img" aria-label="Street map with plumber vans nearby"></div>
    <span class="btn btn--sm">CALL A PLUMBER NOW</span>
  </section>

  <section class="section why">
    <h2 class="heading">WHY CUSTOMERS LOVE<br>PIPEDASHLY?</h2>
    <div class="photo" role="img" aria-label="Photo of a smiling plumber holding a clipboard"></div>
    <div class="perk perk--first">
      <div class="ring"><div class="core"><svg width="64" height="64" viewBox="0 0 64 64"><path d="M22 14c4 0 6 8 4 11l-3 3c2 5 6 9 11 11l3-3c3-2 11 0 11 4v6c0 3-3 4-6 4C27 50 14 37 14 22c0-4 2-8 5-8z" fill="#fff"/></svg></div></div>
      <h4>Available 24/7</h4>
    </div>
    <div class="perk">
      <div class="ring"><div class="core"><svg width="64" height="64" viewBox="0 0 64 64"><path d="M24 10h16l-4 8h-8z" fill="#fff"/><path d="M26 20h12c8 6 14 14 14 22 0 8-6 12-20 12S12 50 12 42c0-8 6-16 14-22z" fill="#fff"/><text x="32" y="47" font-family="Poppins,sans-serif" font-size="20" font-weight="700" fill="#2561a3" text-anchor="middle">$</text></svg></div></div>
      <h4>Up-front Pricing</h4>
    </div>
    <div class="perk">
      <div class="ring"><div class="core"><svg width="64" height="64" viewBox="0 0 64 64"><rect x="12" y="16" width="36" height="36" rx="3" fill="none" stroke="#fff" stroke-width="4"/><path d="M20 32l9 9 24-26" fill="none" stroke="#fff" stroke-width="6"/></svg></div></div>
      <h4>Immediate Response</h4>
    </div>
  </section>
</main>

<main class="screen screen--more">
  <section class="section accreds">
    <div class="badges">
      <div class="badge"><i></i></div>
      <div class="badge"><i></i></div>
      <div class="badge"><i></i></div>
      <div class="badge"><i></i></div>
    </div>
    <h2 class="heading">WE’RE EXPANDING INTO ALL<br>THE MAJOR &nbsp;BOROUGHS IN<br>LONDON &amp; ESSEX</h2>
    <div class="boroughs">
      <ul><li>Barking &amp; Dagenham</li><li>Barnet</li><li>Bexley</li><li>Brent</li><li>Bromley</li><li>Camden</li><li>Croydon</li><li>Ealing</li><li>Enfield</li><li>Greenwich</li><li>Hackney</li><li>Hammersmith &amp; Fulham</li><li>Haringey</li><li>Harrow</li><li>Havering</li><li>Hillingdon</li></ul>
      <ul><li>Hounslow</li><li>Islington</li><li>Kensington &amp; Chelsea</li><li>Kingston upon Thames</li><li>Lambeth</li><li>Lewisham</li><li>Merton</li><li>Newham</li><li>Redbridge</li><li>Richmond upon Thames</li><li>Southwark</li><li>Sutton</li><li>Tower Hamlets</li><li>Waltham Forest</li><li>Wandsworth</li><li>Westminster</li></ul>
    </div>
  </section>

  <section class="section feedback">
    <h2 class="heading">CUSTOMER FEEDBACK</h2>
    <p class="sub">We serve customers instantly<br>across the whole of London.</p>
    <div class="review">
      <div class="quote">“</div>
      <p>Lorem ipsum dolor sit amet, consectetur adipiscing elit, sed do eiusmod tempor incididunt ut labore et dolore magna aliqua. Ut enim ad minim veniam, quis nostrud exercitation ullamco laboris eu fugiat nulla pariatur.</p>
      <span class="name">Megan, Hackney</span>
      <span class="stars">★★★★★</span>
    </div>
    <div class="dots"><span></span><span></span><span></span><span></span><span></span></div>
  </section>

  <section class="section faq">
    <h2 class="heading">FAQ’S</h2>
    <ul class="faq-list">
      <li class="open">How can you verify that PipeDashly plumbers are reliable?<span class="pm"></span></li>
      <li>Are your plumbers on a recognised safety register?<span class="pm"></span></li>
      <li>Do your plumbers have insurance?<span class="pm"></span></li>
      <li>How much do your plumbers cost?<span class="pm"></span></li>
      <li>Do you charge a call-out fee?<span class="pm"></span></li>
      <li>What plumbing services do PipeDashly offer?<span class="pm"></span></li>
      <li>Do you offer emergency plumbing services?<span class="pm"></span></li>
      <li>Do you provide a guarantee for your plumbers’ work?<span class="pm"></span></li>
      <li>When and how do you take payment?<span class="pm"></span></li>
    </ul>
    <span class="btn btn--sm">MORE FAQ’S</span>
  </section>

  <footer class="section footer">
    <span class="brand">PipeDashly</span>
    <div class="f-lines">
      Created with <span class="heart"></span> in London<br>
      Registered in England and Wales<br>
      Company Number 123450987<br>
      ICO Registration ZR4412087
    </div>
    <div class="iso"><i></i><span>ISO27001 Compliant</span></div>
    <h3 class="f-head">ADDRESS</h3>
    <div class="addr"><b><svg width="9" height="11" viewBox="0 0 9 11"><path d="M4.5 0.5a4 4 0 0 1 4 4c0 3-4 6-4 6s-4-3-4-6a4 4 0 0 1 4-4z" fill="none" stroke="#fff"/><circle cx="4.5" cy="4.5" r="1.4" fill="#fff"/></svg></b><span>58 Harbour Lane<br>London, SE4 2XP. UK.</span></div>
    <div class="f-cols">
      <div>
        <h3 class="f-head">DISCOVER</h3>
        <ul class="dotlist"><li>Blog Title 1</li><li>Blog Title 2</li><li>Blog Title 3</li><li>Blog Title 4</li><li style="line-height:13px;padding-top:4px">Blog Title 2 on<br>two lines</li></ul>
      </div>
      <div>
        <h3 class="f-head">SOCIAL</h3>
        <ul class="social"><li><i></i>Chatterly</li><li><i></i>Peeply</li><li><i></i>Linkroom</li><li><i></i>Streamly</li></ul>
      </div>
    </div>
    <div class="apps"><span>Phone app</span><span>Tablet app</span></div>
    <p class="legal">PipeDashly.co.uk is a trading name of MyCompany Name Ltd, registered at Companies House in England and Wales under company registration number 4471203.</p>
    <ul class="dotlist policies"><li>Privacy and Cookie Policy</li><li>Terms &amp; Conditions</li><li>Service Terms &amp; Conditions</li><li>Complaints Policy</li><li>Other Policy</li></ul>
    <div class="copybar">© MyCompanyName Ltd. All Rights Reserved.</div>
  </footer>
</main>

</body>
</html>
```